Lantern Petro - needs a business card

Lantern Petro is a U.S. based diesel sourcing and distribution company that supports American oil & gas fields through providing quality product and consistent services.

Target Market(s)

Oil and Gas

Contact Information for Business Card

The background of the card must be white to ensure the logo pops.

Font styles to use
Serif
Sans Serif

Colors

Designer to choose colors to be used in the design.

Requirements
Must have
• Front of Card: Tag line: Lantern Petro, Powering the Nation's Oil & Gas fields.
• Not sure if you guys do this part but just in case...
• Dale Winterholt
• Owner/CEO
• C:701.555.0148
• E:Dwinterholt@lanternpetro.com
• W:Lanternpetro.com
• Locations: Servicing the Powder River, DJ basin and Bakken formations.
• Back of Card: " Frac fueling is what we do. We understand how important diesel fuel is to your operation, which is why our main service line is Frac fueling. We assure our supply and stand by our service"

```html
<!DOCTYPE html>
<html lang="en">
<head>
<meta charset="utf-8">
<title>Lantern Petro – Business Card</title>
<link href="https://fonts.googleapis.com/css2?family=Arimo:wght@400;700&display=swap" rel="stylesheet">
<style>
  :root {
    --navy: #0d2b5e;
    --red: #b10e16;
    --white: #ffffff;
    --stage: #000000;
    --faint: #e6e7e9;
  }
  * { box-sizing: border-box; margin: 0; padding: 0; }
  html, body { width: 1200px; height: 1200px; overflow: hidden; background: var(--stage); }
  body { position: relative; font-family: "Arimo", Arial, sans-serif; }

  .card { position: absolute; left: 178px; width: 849px; height: 520px; background: var(--white); overflow: hidden; }
  .card--front { top: 54px; }
  .card--back { top: 617px; }

  .tagline-band {
    position: absolute; left: 0; top: 0; width: 100%; height: 54px;
    background: var(--red); color: var(--white);
    font-weight: 700; font-size: 25.5px; line-height: 54px; text-align: center; letter-spacing: 0.1px;
    white-space: nowrap;
  }

  .brand { position: absolute; text-align: center; }
  .brand__mark { display: block; margin: 0 auto; border-radius: 50%; background: var(--navy); }
  .brand__name { display: block; color: var(--navy); font-weight: 700; white-space: nowrap; letter-spacing: 1px; }

  .card--front .brand { left: 26px; top: 110px; width: 360px; }
  .card--front .brand__mark { width: 200px; height: 200px; }
  .card--front .brand__name { margin-top: 44px; font-size: 36px; }

  .person { position: absolute; left: 358px; top: 72px; width: 467px; }
  .person__name { color: var(--red); font-size: 46px; font-weight: 400; line-height: 1; white-space: nowrap; -webkit-text-stroke: 0.6px var(--red); text-align: center; }
  .person__title { display: flex; align-items: center; gap: 10px; margin-top: 12px; color: var(--navy); font-size: 25px; }
  .person__title::before, .person__title::after { content: ""; flex: 1; height: 2px; background: var(--navy); }

  .contact { position: absolute; left: 358px; top: 190px; list-style: none; }
  .contact li { display: flex; align-items: center; height: 50px; color: var(--red); font-size: 29px; white-space: nowrap; }
  .contact svg { flex: none; margin-right: 10px; }

  .location-band { position: absolute; left: 0; bottom: 0; width: 849px; height: 80px; }
  .location-band svg.band { position: absolute; left: 0; top: 0; }
  .location-band__text { position: absolute; left: 65px; top: 24px; color: var(--white); font-size: 24.5px; white-space: nowrap; }
  .location-band__pin { position: absolute; left: 16px; top: 14px; }

  .backdrop-circle { position: absolute; left: -40px; top: 40px; width: 520px; height: 520px; border-radius: 50%; background: var(--faint); }

  .card--back .brand { left: 493px; top: 20px; width: 340px; }
  .card--back .brand__mark { width: 190px; height: 190px; }
  .card--back .brand__name { margin-top: 42px; font-size: 34px; }

  .mission {
    position: absolute; left: 0; top: 370px; width: 100%;
    text-align: center; color: var(--red); font-weight: 700; font-size: 25px; line-height: 30.5px;
  }
</style>
</head>
<body>

<section class="card card--front">
  <div class="tagline-band">LANTERN PETRO, POWERING THE NATION’S OIL &amp; GAS FIELDS</div>

  <div class="brand">
    <span class="brand__mark"></span>
    <span class="brand__name">LANTERN PETRO</span>
  </div>

  <div class="person">
    <h1 class="person__name">DALE WINTERHOLT</h1>
    <p class="person__title">OWNER - CEO</p>
  </div>

  <ul class="contact">
    <li>
      <svg width="34" height="46" viewBox="0 0 34 46" aria-hidden="true">
        <rect x="5" y="2" width="24" height="42" rx="3" fill="none" stroke="#b10e16" stroke-width="3"/>
        <line x1="5" y1="9" x2="29" y2="9" stroke="#b10e16" stroke-width="2"/>
        <line x1="5" y1="35" x2="29" y2="35" stroke="#b10e16" stroke-width="2"/>
        <circle cx="17" cy="40" r="2" fill="#b10e16"/>
      </svg>
      701.555.0148
    </li>
    <li>
      <svg width="40" height="28" viewBox="0 0 40 28" aria-hidden="true">
        <rect x="2" y="2" width="36" height="24" fill="none" stroke="#b10e16" stroke-width="2.5"/>
        <polyline points="2,2 20,16 38,2" fill="none" stroke="#b10e16" stroke-width="2.5"/>
        <line x1="2" y1="26" x2="15" y2="12" stroke="#b10e16" stroke-width="2"/>
        <line x1="38" y1="26" x2="25" y2="12" stroke="#b10e16" stroke-width="2"/>
      </svg>
      Dwinterholt@lanternpetro.com
    </li>
    <li>
      <svg width="40" height="40" viewBox="0 0 40 40" aria-hidden="true">
        <g fill="none" stroke="#b10e16" stroke-width="2">
          <circle cx="20" cy="20" r="17"/>
          <ellipse cx="20" cy="20" rx="8" ry="17"/>
          <line x1="20" y1="3" x2="20" y2="37"/>
          <line x1="3" y1="20" x2="37" y2="20"/>
          <path d="M6 11 H34 M6 29 H34"/>
        </g>
      </svg>
      Lanternpetro.com
    </li>
  </ul>

  <div class="location-band">
    <svg class="band" width="849" height="80" viewBox="0 0 849 80" aria-hidden="true">
      <polygon points="0,0 757,0 849,80 0,80" fill="#0d2b5e"/>
      <polygon points="275,58 825,58 849,80 275,80" fill="#b10e16"/>
    </svg>
    <svg class="location-band__pin" width="40" height="60" viewBox="0 0 40 60" aria-hidden="true">
      <g fill="none" stroke="#ffffff" stroke-width="3">
        <path d="M20 38 C10 26 8 20 8 15 A12 12 0 0 1 32 15 C32 20 30 26 20 38 Z"/>
        <circle cx="20" cy="15" r="5"/>
        <path d="M12 40 A14 10 0 1 0 28 40"/>
      </g>
    </svg>
    <p class="location-band__text">Servicing the Powder River, DJ basin and Bakken formations</p>
  </div>
</section>

<section class="card card--back">
  <span class="backdrop-circle" aria-hidden="true"></span>

  <div class="brand">
    <span class="brand__mark"></span>
    <span class="brand__name">LANTERN PETRO</span>
  </div>

  <p class="mission">
    Frac fueling is what we do.<br>
    We understand how important diesel fuel is to your operation,<br>
    which is why our main service line is Frac fueling.<br>
    We assure our supply and stand by our service
  </p>
</section>

</body>
</html>
```